Q&W Night club Presents :

I need a advertiser 4 nights in one poster, from Thursday to Sunday,
Thursday : Every Thursday Irish Night
Friday: Old School Hip Hop, top 40 & request
Sat: Ripple Saturdays July 11, July 25, August 8, August 22
Brazilian Night Forro: July 18, August 1, August 15 & August 29
Sunday: Velvet Sundaze ( Dj Marlow & Dj Brevo

Target Market(s)

All 4 Nights

Industry/Entity Type

School

Font styles to use
Decorative
Script

Requirements
Must have
• Poster 11x16 and talk about all 4 nights on, see up there description
Nice to have
• A lot of colors
Should not have
• Address: 213 Calloway Rd Hyannis MA
• 5085550172
• Starting 9:30pm until 1:00Am
• 21+ ID
• Special Drinks $3.99

```html
<!DOCTYPE html>
<html lang="en">
<head>
<meta charset="utf-8">
<title>Q&amp;W Nightclub Presents</title>
<link rel="stylesheet" href="https://fonts.googleapis.com/css2?family=Montserrat:wght@800;900&family=Fredoka:wght@500;600;700&display=swap">
<style>
  :root {
    --ink: #000;
    --gold-light: #f6d87a;
    --gold-mid: #d9a93a;
    --gold-dark: #a9731c;
    --sky-light: #8fd3ff;
    --sky-dark: #2a6fa8;
    --steel: #5d7f95;
    --lime-light: #b8f27a;
    --lime-dark: #3aa13a;
    --magenta-light: #ff9cf0;
    --magenta-dark: #c22fb8;
    --sun-yellow: #ffd21f;
    --sun-orange: #ffb514;
    --coral: #ff6a3d;
    --coral-deep: #f0453a;
    --cream: #f3e1a3;
    --glow-pink: #ffd3ff;
    --glow-green: #3aa13a;
    --glow-indigo: #3a1f8f;
  }
  * { margin: 0; padding: 0; box-sizing: border-box; }
  html, body { width: 880px; height: 1200px; overflow: hidden; background: var(--ink); }
  .poster { position: relative; width: 880px; height: 1200px; overflow: hidden; background: var(--ink); }

  .club-lights {
    position: absolute; inset: 0 0 auto 0; height: 700px;
    background:
      radial-gradient(ellipse 230px 210px at 440px 340px, var(--glow-pink) 0%, rgba(255,180,255,.6) 35%, transparent 75%),
      radial-gradient(ellipse 200px 220px at 190px 480px, rgba(20,201,192,.9) 0%, transparent 80%),
      radial-gradient(ellipse 220px 220px at 770px 460px, rgba(240,150,40,.9) 0%, transparent 80%),
      radial-gradient(ellipse 340px 320px at 480px 310px, rgba(226,63,208,.85) 0%, transparent 80%),
      linear-gradient(120deg, var(--glow-indigo) 0%, #6a1a6a 30%, #b04a50 50%, #8a7a20 70%, var(--glow-green) 100%);
    -webkit-mask-image: linear-gradient(to bottom, #000 65%, transparent 100%);
            mask-image: linear-gradient(to bottom, #000 65%, transparent 100%);
  }

  .headline-block { position: absolute; top: 104px; left: 0; width: 100%; text-align: center; }
  .headline { font-family: "Montserrat", sans-serif; font-weight: 900; font-size: 66px; letter-spacing: 2px; line-height: 83px; white-space: nowrap; }

  .gold {
    background: linear-gradient(to bottom, var(--gold-light) 0%, var(--gold-mid) 50%, var(--gold-dark) 100%);
    -webkit-background-clip: text; background-clip: text; color: transparent;
  }
  .lime {
    background: linear-gradient(to bottom, var(--lime-light) 0%, var(--lime-dark) 100%);
    -webkit-background-clip: text; background-clip: text; color: transparent;
  }
  .sky {
    background: linear-gradient(to bottom, var(--sky-light) 0%, var(--sky-dark) 55%, var(--steel) 100%);
    -webkit-background-clip: text; background-clip: text; color: transparent;
  }
  .magenta {
    background: linear-gradient(to bottom, var(--magenta-light) 0%, var(--magenta-dark) 100%);
    -webkit-background-clip: text; background-clip: text; color: transparent;
  }

  .nights {
    position: absolute; top: 596px; left: 0; width: 100%;
    display: flex; flex-direction: column; align-items: center; text-align: center;
  }
  .night { display: flex; flex-direction: column; align-items: center; }
  .night > * { white-space: nowrap; }

  .day-name { font-family: "Montserrat", sans-serif; font-weight: 900; font-size: 46px; line-height: 50px; }
  .night-title { font-family: "Montserrat", sans-serif; font-weight: 800; font-size: 28px; line-height: 34px; }
  .night-detail { font-family: "Fredoka", sans-serif; font-weight: 600; font-size: 22px; line-height: 28px; color: var(--cream); }
  .night-title--second { margin-top: 6px; }

  .sunday-name { font-family: "Fredoka", sans-serif; font-weight: 700; font-size: 50px; line-height: 54px; color: var(--sun-yellow); }
  .sunday-title { font-family: "Fredoka", sans-serif; font-weight: 700; font-size: 42px; line-height: 46px; color: var(--sun-orange); }
  .sunday-djs {
    font-family: "Fredoka", sans-serif; font-weight: 700; font-size: 30px; line-height: 36px;
    background: linear-gradient(to bottom, var(--coral) 0%, var(--coral-deep) 100%);
    -webkit-background-clip: text; background-clip: text; color: transparent;
  }

  .divider { width: 328px; height: 1px; margin: 13px 0;
    background: linear-gradient(to right, transparent, var(--gold-mid) 20%, var(--gold-light) 50%, var(--gold-mid) 80%, transparent); }
</style>
</head>
<body>
<main class="poster">
  <div class="club-lights" role="img" aria-label="Silhouetted crowd dancing with raised arms under colourful club lights"></div>

  <header class="headline-block">
    <h1 class="headline gold">Q&amp;W NIGHTCLUB</h1>
    <p class="headline gold">PRESENTS</p>
  </header>

  <div class="nights">
    <section class="night">
      <h2 class="day-name gold">THURSDAY</h2>
      <p class="night-title gold">EVERY THURSDAY IRISH NIGHT</p>
    </section>
    <div class="divider"></div>

    <section class="night">
      <h2 class="day-name lime">FRIDAY</h2>
      <p class="night-detail">Old School Hip Hop, Top 40 &amp; Request</p>
    </section>
    <div class="divider"></div>

    <section class="night">
      <h2 class="day-name sky">SATURDAY</h2>
      <p class="night-title sky">RIPPLE SATURDAYS</p>
      <p class="night-detail">July 11 · July 25 · August 8 · August 22</p>
      <p class="night-title night-title--second magenta">BRAZILIAN NIGHT FORRÓ</p>
      <p class="night-detail">July 18 · August 1 · August 15 &amp; August 29</p>
    </section>
    <div class="divider"></div>

    <section class="night">
      <h2 class="sunday-name">Sunday</h2>
      <p class="sunday-title">Velvet Sundaze</p>
      <p class="sunday-djs">Dj Marlow &amp; Dj Brevo</p>
    </section>
  </div>
</main>
</body>
</html>
```